Business card design needed to incorporate existing logo

We need a business card for a new modern Accounting & Business Solutions company call KelvaTrade Services.com.au servicing all of Australia.
My tagline is Steady Ledger Answers... built right.

We specialise in Cloud Accounting and this is our primary focus. We also provide tax representation, debt recovery, computer, tablet and smart phone sales.

I would like a design that uses my corporate, trustworthy colours of blue/white, black/grey however am open to suggestion. I have attached my logo to go on the card somewhere,of which you will see the colour scheme.

I am after a card that STANDS OUT, somewhere between it not being too busy and not being a baron waste of space.

A 'cloud' incorporated in the design may work well, up to your artistic judgement. I know what I like when I see it; it is harder to put into words!

Excited to see your ideas!
I have added my logo predominately (blue/white) and for additional opportunity have added my reverse logo (darker one). I have used the blue/white on my website and letterhead. I will be using both on my vehicle signage.

Target Market(s)

Tradesmen and small-medium businesses of all descriptions Australia-wide

Industry/Entity Type

Debt

Contact Information for Business Card

Dale Pemberton
Principal (optional)
KelvaTrade Services.com.au
Steady Ledger Answers... built right

P: 1800 513 684
M: 0412 860 571 (optional)
W: www.kelvatradeservices.com.au
E: admin@kelvatradeservices.com.au

Logo Text

Steady Ledger Answers... built right!

Logo styles of interest
Wordmark Logo
Requirements
Must have
• Must look professional and of high quality not cheap.

My logo and my tagline 'Steady Ledger Answers... built right'.

I have my colourscheme in mind as per my attached logo, however am open to suggestion. I want to see what you can create that I would not have thought of.

Modern, innovative.
Something I won't look at and think, 'I could have done that myself'.

Must be able to be printed on Norla 300gm premium cards and the artwork provided to me.
Nice to have
• Title of Principal is optional depending on space and judement call of look/fee.
M: (mobile) number is also optional as above.

Somthing cloud related given the Cloud Accounting aspect may be relevant. I leave it to your artistic design and judgement.
Should not have
• Must not look cheap.

```html
<!DOCTYPE html>
<html lang="en">
<head>
<meta charset="utf-8">
<title>KelvaTrade Services – Business Card</title>
<link rel="stylesheet" href="https://fonts.googleapis.com/css2?family=Questrial&display=swap">
<style>
  :root {
    --navy: #1f2a5c;
    --mid-blue: #246a98;
    --card-white: #f2f2f3;
    --card-edge: #dcdcde;
    --brand-blue: #2a6fb0;
    --ink: #1e2452;
    --backdrop: #e6e6e8;
    --text-light: #ffffff;
  }
  * { margin: 0; padding: 0; box-sizing: border-box; }
  html, body {
    width: 1200px; height: 1181px; overflow: hidden;
    background: var(--backdrop);
    font-family: "Questrial", "Century Gothic", sans-serif;
  }
  .canvas { position: relative; width: 1200px; height: 1181px; }

  .card {
    position: absolute; left: 233px; width: 735px; height: 430px;
    background: radial-gradient(ellipse at 50% 50%, #ffffff 0%, var(--card-white) 55%, var(--card-edge) 100%);
    box-shadow: 0 6px 14px rgba(0,0,0,0.25);
    overflow: hidden;
  }
  .card--front { top: 129px; }
  .card--back  { top: 612px; }

  .top-band { position: absolute; top: 0; left: 0; right: 0; height: 12px; background: var(--navy); }

  .bottom-strip {
    position: absolute; bottom: 0; left: 0; right: 0; height: 13px;
    display: grid; grid-template-columns: 240px 249px 240px; column-gap: 3px;
  }
  .bottom-strip span { background: var(--navy); }
  .bottom-strip span.accent { background: var(--mid-blue); }

  .brand {
    position: absolute; top: 165px; left: 0; right: 0;
    display: flex; align-items: center; justify-content: center; gap: 18px;
  }
  .brand__dot { width: 46px; height: 46px; border-radius: 50%; background: var(--brand-blue); }
  .brand__name {
    font-size: 40px; letter-spacing: 3px; color: var(--brand-blue); font-weight: 400;
  }

  .tagline {
    position: absolute; left: 0; right: 0; text-align: center;
    color: var(--ink); font-size: 15px; font-weight: 700; letter-spacing: 0.2px;
  }
  .tagline--lead { top: 52px; }
  .tagline--close { top: 260px; }

  .emblem {
    position: absolute; left: 287px; top: 88px; width: 162px; height: 162px;
    border-radius: 50%; background: var(--brand-blue);
  }

  .contact-panel {
    position: absolute; left: 0; right: 0; bottom: 0; height: 124px;
    background: var(--navy);
  }
  .contact-panel__rule { position: absolute; top: 12px; left: 0; right: 0; height: 2px; background: #ffffff; }
  .contact-panel__cols {
    position: absolute; top: 14px; left: 0; right: 0; bottom: 0;
    display: grid; grid-template-columns: 240px 249px 240px; column-gap: 3px;
    background: #ffffff;
  }
  .contact-col {
    background: var(--navy); color: var(--text-light);
    display: flex; flex-direction: column; align-items: center; justify-content: center;
    font-size: 13px; line-height: 16px; padding-bottom: 8px;
  }
  .contact-col--name { background: var(--mid-blue); }
  .person { font-size: 20px; line-height: 22px; font-weight: 700; }
  .role { font-size: 12px; letter-spacing: 5px; line-height: 18px; }
</style>
</head>
<body>
<div class="canvas">

  <section class="card card--front" aria-label="Card front">
    <div class="top-band"></div>
    <div class="brand">
      <span class="brand__dot"></span>
      <span class="brand__name">KelvaTrade Services.com.au</span>
    </div>
    <div class="bottom-strip"><span></span><span class="accent"></span><span></span></div>
  </section>

  <section class="card card--back" aria-label="Card back">
    <div class="top-band"></div>
    <p class="tagline tagline--lead">Steady Ledger Answers ...</p>
    <div class="emblem"></div>
    <p class="tagline tagline--close">built right</p>
    <div class="contact-panel">
      <div class="contact-panel__rule"></div>
      <div class="contact-panel__cols">
        <div class="contact-col">
          <span>M : 0412 860 571</span>
          <span>admin@kelvatradeservices.com.au</span>
        </div>
        <div class="contact-col contact-col--name">
          <span class="person">Dale Pemberton</span>
          <span class="role">Principal</span>
        </div>
        <div class="contact-col">
          <span>P : 1800 513 684</span>
          <span>www.kelvatradeservices.com.au</span>
        </div>
      </div>
    </div>
  </section>

</div>
</body>
</html>
```